Flyer-Design für Keramik Verdunster
Zielgruppe
Wir wollen Keramik Verdunster bei Volkarn Verkaufen und dieser Flyer soll in jede Produktverpackung mit hinein gelegt werden.
Aufgabenstellung
Der Flyer sollte möglichst klein gehalten werden, also mehrmals Faltbar. Kann auf Vorder- und Rückseite bedruckt werden.
Ihrer Kreativität sind von unserer seite aus ,keine Grenzen gesetzt.
Im Anhang unser Logo , was mit auf den Flyer muss und in der Worddatei haben wir in Klammern noch Instruktionen für sie mit reingeschrieben. Design ect. ist Ihnen überlassen

```html
<!DOCTYPE html>
<html lang="de">
<head>
<meta charset="utf-8">
<title>Sorental – Anleitung Raumklima</title>
<link href="https://fonts.googleapis.com/css2?family=Roboto+Condensed:wght@300;400;700&display=swap" rel="stylesheet">
<style>
  :root{
    --ink:#1d1d1b;
    --text:#333333;
    --blue:#1a95d3;
    --rule:#c9c9c9;
    --navy:#1f3a63;
    --gold:#f3b31b;
    --paper:#ffffff;
  }
  *{box-sizing:border-box;margin:0;padding:0}
  html,body{width:865px;height:1200px;overflow:hidden;background:var(--paper)}
  body{font-family:"Roboto Condensed",Arial,sans-serif;color:var(--text);font-weight:300;font-size:9px;line-height:17.6px;position:relative}
  .sheet{position:absolute;inset:0;border:1px solid var(--ink)}
  .block{position:absolute}
  h1,h2,h3{color:var(--ink);font-weight:700}
  .h-main{font-size:11.5px;line-height:16px}
  .h-large{font-size:12.5px;line-height:21px}
  .h-sub{font-size:9.5px;line-height:17.6px}
  strong{font-weight:700;color:var(--ink)}
  p{margin:0}
  .brand{position:absolute;text-align:center;color:var(--navy)}
  .brand-dot{display:block;margin:0 auto;border-radius:50%;background:var(--navy)}
  .brand-name{font-weight:400;letter-spacing:3px}
  .brand--top{left:686px;top:36px;width:130px}
  .brand--top .brand-dot{width:46px;height:46px}
  .brand--top .brand-name{font-size:15px;margin-top:12px}
  .brand--foot{left:44px;top:1116px;width:72px}
  .brand--foot .brand-dot{width:30px;height:30px}
  .brand--foot .brand-name{font-size:9.5px;margin-top:6px;letter-spacing:2px}
  .footer-note{position:absolute;left:186px;top:1156px;font-size:8.5px;font-weight:700;color:var(--ink)}
  table{border-collapse:collapse;width:100%}
  .climate th,.climate td{font-size:8.5px;line-height:18px;padding:0 2px}
  .climate .cap{color:var(--blue);font-weight:700;text-align:center;border-top:1.5px solid var(--blue)}
  .climate .cols th{color:var(--ink);font-weight:700;border-bottom:1.5px solid var(--blue)}
  .climate td{border-bottom:1px solid var(--rule)}
  .climate tr:last-child td{border-bottom:1.5px solid var(--blue)}
  .climate .c{text-align:center}
  .airing{width:158px}
  .airing th,.airing td{font-size:8.5px;line-height:18.6px;text-align:left;border-bottom:1px dotted #777;padding:0 4px}
  .airing th{color:var(--blue);font-weight:700;border-top:1px dotted #777}
  .airing td:last-child,.airing th:last-child{padding-left:24px}
  .cta{position:absolute;left:451px;top:876px;width:334px;height:48px;background:var(--blue);color:#fff;font-weight:700;font-size:11px;line-height:19px;padding:5px 0 0 14px}
  .stars{position:absolute;left:566px;top:940px}
</style>
</head>
<body>
<div class="sheet">

  <div class="brand brand--top"><span class="brand-dot"></span><div class="brand-name">SORENTAL</div></div>

  <section class="block" style="left:44px;top:146px;width:372px">
    <h1 class="h-main">Anleitung für ein ideales Raumklima</h1>
    <h2 class="h-sub" style="margin-top:22px">Was muss ich beachten und wie funktionieren meine neuen Sorental Heizkörper Luft-<br>befeuchter.</h2>
    <p style="margin-top:12px">[GRAFIK MIT RAND EVTL.]</p>
    <p><strong>1.</strong> Füllen Sie Ihre neuen Luftbefeuchter mit warmen Wasser, idealerweise mit entkalktem Wasser.</p>
    <p><strong>2.</strong> Sollten Sie kein entkalktes Wasser haben , sollten Sie Ihre Verdunster nach jedem Durchgang (Komplett Verdunstet) mit verdünntem Essig oder Zitronensäure von Innen reinigen, um die Poren Kalkfrei zu halten und um eine optimale Verdunstung zu gewährleisten.</p>
    <p><strong>3.</strong> Um weiterhin eine optimale Verdunstung zu gewährleisten, sollte Ihr Heizkörper so Warm sein, dass Sie ihn gerade noch mit der Hand anfassen können oder noch heißer.</p>
    <p><strong>4.</strong> Bringen Sie an jedem Heizkörper zwei Verdunster an. Außer im Bad und der Küche!</p>
    <p><strong>5.</strong> Wenn die Verdunster zu lange an einem Heizkörper hängen, die abgeschaltet bzw. kalt sind, dann kann es zur Tröpfchenbildung kommen, weil die Poren groß sind und bei kalter Oberfläche kann das Wasser nicht schnell genug verdunsten.</p>
    <p style="margin-top:16px"><strong>MERKE!</strong></p>
    <p>Die Verdunstungsdauer hängt von den verschiedensten Faktoren ab. Je gesättigter Ihre rel. Luft-feuchtigkeit im Raum (durch schlechtes Lüften) und je kälter der Heizkörper desto Länger dauert der Verdunstungsprozess! Die Luft kann dadurch nicht mehr Feuchtigkeit aufnehmen!</p>
  </section>

  <section class="block" style="left:44px;top:568px;width:372px">
    <h2 class="h-large">Anleitung für ein Ideales Raumklima und die optimale Luftfeuchtigkeit mit Ihrem Sorental Heizkörper Luftbefeuchter!</h2>
    <p style="margin-top:14px">Für ein schönes Klima sorgen Sie, wie Folgt:</p>
    <p style="margin-top:10px"><strong>Tabelle: relative Luftfeuchtigkeit in Wohnräumen</strong></p>
    <p>In der folgenden Tabelle finden Sie die optimalen Werte für relative Luftfeuchte und Temperatur in den verschiedenen Wohnbereichen.</p>
    <table class="climate" style="margin-top:12px">
      <tr><th class="cap" colspan="3">Ideales Raumklima</th></tr>
      <tr class="cols"><th style="text-align:left">Raum</th><th>Optimale Temperatur</th><th>Optimale Luftfeuchtigkeit</th></tr>
      <tr><td>Wohnräume</td><td class="c">20 °C</td><td class="c">40 - 60 %</td></tr>
      <tr><td>Schlafzimmer</td><td class="c">16 - 18 °C</td><td class="c">40 - 60 %</td></tr>
      <tr><td>Kinderzimmer</td><td class="c">20 - 22 °C</td><td class="c">40 - 60 %</td></tr>
      <tr><td>Küche</td><td class="c">18 °C</td><td class="c">50 - 70 %</td></tr>
      <tr><td>Badezimmer</td><td class="c">23 °C</td><td class="c">50 - 70 %</td></tr>
    </table>
    <p style="margin-top:16px">Als ideale Mittelwerte haben sich 40 - 60 % Feuchte und 20 °C Raumtemperatur bewährt.</p>
    <p style="margin-top:14px">Naturgemäß liegt die Luftfeuchte in Küche und Bad etwas höher und kann beim Kochen oder Du-schen auch über diese Werte steigen.</p>
    <p>Das ist kein Problem, solange der Zustand nicht dauerhaft anhält. Dennoch sollte es Ihnen zur Ge-wohnheit werden, sofort nach dem Kochen oder Duschen den Wasserdampf nach draußen entwei-chen zu lassen.</p>
  </section>

  <section class="block" style="left:458px;top:146px;width:370px">
    <h2 class="h-main">Wissenswertes zur Luftfeuchtigkeit</h2>
    <p style="margin-top:22px">Das gesündeste Raumklima herrscht bei 50 % relativer Luftfeuchte und 20 °C Raumtemperatur.<br>Die relative Raumfeuchte sollte nicht unter 30 % fallen.<br>Einige Schimmelpilzarten vermehren sich bereits ab 70 % Feuchtigkeit.<br>Herrschen über einen längeren Zeitraum mehr als 80 % Feuchtigkeit im Raum, führt das unver-meidlich zur Entstehung von Schimmel.</p>
    <h2 class="h-main" style="margin-top:40px">Richtiges Lüften</h2>
    <p style="margin-top:22px">Schließen Sie den Thermostatkopf der Heizungen komplett. Öffnen Sie die Fenster zweier gegen-überliegender Räume gleichzeitig und lassen auch die Türen offen stehen. Auf diese Weise ent-steht ein Durchzug und die warme, verbrauchte Luft zieht schneller nach draußen ab. Achtung: Vergessen Sie nicht, auch im zweiten Raum, den Heizkörper während des Lüftens abzustellen! Wie oft sollten Sie Lüften? Optimal wäre 4 mal am Tag, da dies aber oft nicht möglich ist, sollten Sie mindestens 2 mal am Tag Lüften, Abends vor dem Schlafen gehen und Morgens nach dem Aufstehen.</p>
    <p style="margin-top:20px;color:var(--blue);font-weight:700">Dauer des Lüftens:</p>
    <table class="airing">
      <tr><th>Monat</th><th>Dauer</th></tr>
      <tr><td>Januar</td><td>5 min</td></tr>
      <tr><td>Februar</td><td>5 min</td></tr>
      <tr><td>März</td><td>10 min</td></tr>
      <tr><td>April</td><td>15 min</td></tr>
      <tr><td>Mai</td><td>20 min</td></tr>
      <tr><td>Juni</td><td>30 min</td></tr>
      <tr><td>Juli</td><td>30 min</td></tr>
      <tr><td>August</td><td>30 min</td></tr>
      <tr><td>September</td><td>15 min</td></tr>
      <tr><td>Oktober</td><td>20 min</td></tr>
      <tr><td>November</td><td>10 min</td></tr>
      <tr><td>Dezember</td><td>5 min</td></tr>
    </table>
    <p style="margin-top:20px">Wenn Sie nun so vorgehen wie beschrieben, wird Ihnen und dem wunderbaren Gefühl eines<br>&nbsp;schönen Klimas im Zuhause &nbsp;,nichts mehr im Wege stehen.</p>
  </section>

  <div class="cta">Sie sind zufrieden mit unserem Produkt und dieser Anleitung?<br>Dann Hinterlassen Sie uns doch bitte eine Rezension auf Volkarn.</div>

  <svg class="stars" width="112" height="22" viewBox="0 0 112 22" aria-label="Fünf Sterne">
    <defs>
      <polygon id="star" points="11,1 13.9,7.6 21,8.2 15.6,12.9 17.2,20 11,16.2 4.8,20 6.4,12.9 1,8.2 8.1,7.6" fill="var(--gold)" stroke="#c98a0a" stroke-width="0.8"/>
    </defs>
    <use href="#star" x="0"/><use href="#star" x="22.5"/><use href="#star" x="45"/><use href="#star" x="67.5"/><use href="#star" x="90"/>
  </svg>

  <div class="brand brand--foot"><span class="brand-dot"></span><div class="brand-name">SORENTAL</div></div>
  <div class="footer-note">SORENTAL_ ADRESSE_ZUSATZ_BLINDTEXT FUER WEITERE ANGABEN VON SORENTAL</div>

</div>
</body>
</html>
```